Larkspur Realty

Business cards for 4 people

They need to say for all
57 Danner Quay, Boston MA 02117

Each person will have their own personal information
We would like gold embossing for the name of the company
Mabel is the blonde sitting in the chair smiling her information should be on the back of the card with her name and information
Should say for slogan classic pattern, elevated experience
mabel@larkspurhomesnet.com
(413) 555-0182

Odessa is the brunette with wavy hair in the tan suit odessa@larkspurhomesnet.com
(617) 555-0147

june@larkspurhomesnet.com
(413) 555-0169
standing next to the chair

ruth@larkspurhomesnet.com
(413) 555-0193
close up headshot

```html
<!DOCTYPE html>
<html lang="en">
<head>
<meta charset="utf-8">
<title>Larkspur Realty — Business Card</title>
<link href="https://fonts.googleapis.com/css2?family=Montserrat:wght@400;500;700&display=swap" rel="stylesheet">
<style>
  :root {
    --backdrop: #e4e4e2;
    --navy-deep: #1d2946;
    --navy-light: #34435f;
    --navy-text: #1c2540;
    --gold: #e0a955;
    --grey-text: #7a7a7a;
    --card-white: #f4f4f4;
    --card-shade: #e2e2e2;
    --photo-tone: #c9c4c2;
  }
  * { margin: 0; padding: 0; box-sizing: border-box; }
  html, body {
    width: 1200px; height: 1200px; overflow: hidden;
    background: var(--backdrop);
    font-family: "Montserrat", Arial, sans-serif;
  }
  .canvas { position: relative; width: 1200px; height: 1200px; }

  .card {
    position: absolute; left: 234px; width: 731px; height: 418px;
  }
  .card-front {
    top: 160px;
    background: linear-gradient(225deg, var(--navy-light), var(--navy-deep) 70%);
    display: flex; flex-direction: column; align-items: center; justify-content: center;
  }
  .brand-mark {
    width: 104px; height: 104px; border-radius: 50%;
    border: 3px solid var(--gold); margin-bottom: 24px;
  }
  .brand-name {
    color: var(--gold); font-weight: 500; font-size: 34px;
    letter-spacing: 4px; text-transform: uppercase;
  }

  .card-back {
    top: 632px;
    background: linear-gradient(200deg, var(--card-white), var(--card-shade));
  }
  .portrait {
    position: absolute; left: 48px; top: 166px; width: 164px; height: 164px;
    border-radius: 50%; border: 3px solid var(--gold);
    background: radial-gradient(circle at 45% 40%, #d9d4d2, var(--photo-tone) 55%, #3a3536);
  }
  .divider {
    position: absolute; left: 130px; top: 329px; width: 546px; height: 2px;
    background: var(--gold);
  }
  .person-name {
    position: absolute; left: 241px; top: 176px;
    font-size: 40px; font-weight: 700; color: var(--gold); line-height: 1;
  }
  .person-title {
    position: absolute; left: 239px; top: 220px;
    font-size: 23px; color: var(--grey-text); line-height: 1;
  }
  .contact-row {
    position: absolute; left: 239px; display: flex; align-items: center; gap: 10px;
    font-size: 24px; color: var(--grey-text); line-height: 1;
  }
  .contact-row svg { width: 21px; height: 21px; flex: none; fill: var(--gold); }
  .row-phone { top: 258px; }
  .row-email { top: 293px; letter-spacing: 2px; }
  .row-email .domain { color: var(--navy-text); }
  .row-address { top: 343px; }
</style>
</head>
<body>
<main class="canvas">
  <section class="card card-front">
    <div class="brand-mark"></div>
    <div class="brand-name">Larkspur Realty</div>
  </section>

  <section class="card card-back">
    <div class="portrait" role="img" aria-label="Portrait photo of Ruth Calloway"></div>
    <div class="divider"></div>
    <div class="person-name">Ruth Calloway</div>
    <div class="person-title">Co-creative Director</div>

    <div class="contact-row row-phone">
      <svg viewBox="0 0 24 24" aria-hidden="true"><path d="M6.6 10.8a15 15 0 0 0 6.6 6.6l2.2-2.2c.3-.3.7-.4 1-.2 1.1.4 2.3.6 3.6.6.6 0 1 .4 1 1V20c0 .6-.4 1-1 1A17 17 0 0 1 3 4c0-.6.4-1 1-1h3.5c.6 0 1 .4 1 1 0 1.3.2 2.5.6 3.6.1.3 0 .7-.2 1z"/></svg>
      <span>(413) 555-0193</span>
    </div>
    <div class="contact-row row-email">
      <svg viewBox="0 0 24 24" aria-hidden="true"><path d="M2 5h20v2l-10 6L2 7z M2 9l10 6 10-6v10H2z"/></svg>
      <span>ruth@<span class="domain">larkspurhomesnet.com</span></span>
    </div>
    <div class="contact-row row-address">
      <svg viewBox="0 0 24 24" aria-hidden="true"><path d="M12 2a7 7 0 0 0-7 7c0 5 7 13 7 13s7-8 7-13a7 7 0 0 0-7-7zm0 9.5a2.5 2.5 0 1 1 0-5 2.5 2.5 0 0 1 0 5z"/></svg>
      <span>57 Danner Quay, Boston MA 02117</span>
    </div>
  </section>
</main>
</body>
</html>
```